Lumo -Fresh business card design

It is a dry cleaning carpet business.
Red wine stain removal and pet urine treatments.
Servicing all regional areas.

all logo and pictures files have been uploaded

Industry/Entity Type

Dry Cleaning

Contact Information for Business Card

Lumo-Fresh Carpet and upholstery cleaning.
Servicing Albury/Wodonga and surrounding areas.
ph greg 0413572960 ,email lumofresh1@kestrelmail.com

Font styles to use
Serif
Sans Serif
Other font styles liked:
• lumo fresh logo font

Colors
ec2027
ffcf3e
33a6d7
0692cd

Requirements
Nice to have
• I have included photos of the logo and car and stripe on van ,I dont need all of them in the card just i would like to stick to these colours.

```html
<!DOCTYPE html>
<html lang="en">
<head>
<meta charset="utf-8">
<title>Lumo-Fresh Business Card</title>
<link href="https://fonts.googleapis.com/css2?family=Michroma&family=Oswald:wght@500;700&family=Open+Sans:wght@600&display=swap" rel="stylesheet">
<style>
  :root {
    --backdrop: #3b3b3d;
    --card-white: #ffffff;
    --blue-light: #1b8fdc;
    --blue-deep: #2d5cbf;
    --brand-blue: #33a6d7;
    --tagline-blue: #5b86c9;
    --text-light: #ffffff;
  }
  html, body {
    margin: 0;
    padding: 0;
    width: 1200px;
    height: 816px;
    overflow: hidden;
    background: var(--backdrop);
  }
  .canvas {
    position: relative;
    width: 1200px;
    height: 816px;
    overflow: hidden;
    background: var(--backdrop);
  }
  .card {
    position: absolute;
    left: 100px;
    top: 122px;
    width: 1000px;
    height: 572px;
    border-radius: 40px;
    overflow: hidden;
    background: var(--card-white);
  }
  .card__panel {
    position: absolute;
    inset: 0;
    width: 1000px;
    height: 572px;
  }
  .brand {
    position: absolute;
    left: 0;
    top: 200px;
    width: 380px;
    text-align: center;
  }
  .brand__name {
    margin: 0;
    font-family: "Oswald", sans-serif;
    font-weight: 700;
    font-size: 62px;
    line-height: 1;
    letter-spacing: 1px;
    color: var(--brand-blue);
  }
  .brand__tagline {
    margin: 12px 0 0;
    font-family: "Open Sans", sans-serif;
    font-weight: 600;
    font-size: 20px;
    line-height: 1.2;
    color: var(--tagline-blue);
  }
  .contact {
    position: absolute;
    left: 440px;
    top: 70px;
    margin: 0;
    padding: 0;
    list-style: none;
    font-family: "Michroma", sans-serif;
    font-size: 15px;
    letter-spacing: 1.5px;
    color: var(--text-light);
  }
  .contact__item {
    display: flex;
    align-items: flex-start;
    gap: 14px;
    margin-bottom: 22px;
    line-height: 1.5;
  }
  .contact__icon {
    flex: none;
    width: 18px;
    height: 18px;
    margin-top: 2px;
  }
  .divider {
    position: absolute;
    left: 440px;
    top: 352px;
    width: 470px;
    border-top: 3px dotted rgba(255,255,255,0.85);
  }
  .person {
    position: absolute;
    right: 90px;
    top: 372px;
    text-align: right;
    color: var(--text-light);
    font-family: "Oswald", sans-serif;
    text-transform: uppercase;
  }
  .person__name {
    margin: 0;
    font-weight: 500;
    font-size: 44px;
    line-height: 1.1;
    letter-spacing: 1px;
  }
  .person__role {
    margin: 2px 0 0;
    font-weight: 500;
    font-size: 26px;
    letter-spacing: 1px;
  }
</style>
</head>
<body>
<main class="canvas">
  <article class="card">
    <svg class="card__panel" viewBox="0 0 1000 572" aria-hidden="true">
      <defs>
        <linearGradient id="panelGradient" x1="0" y1="0" x2="1" y2="1">
          <stop offset="0" stop-color="#1b8fdc"/>
          <stop offset="1" stop-color="#2d5cbf"/>
        </linearGradient>
      </defs>
      <path d="M380 0 H1000 V572 H380 V420 L362 408 L362 392 L380 392 Z" fill="url(#panelGradient)"/>
    </svg>

    <div class="brand">
      <h1 class="brand__name">LUMO-FRESH</h1>
      <p class="brand__tagline">CARPET &amp; UPHOLSTERY<br>CLEANING</p>
    </div>

    <ul class="contact">
      <li class="contact__item">
        <svg class="contact__icon" viewBox="0 0 24 24"><path fill="#fff" d="M6.6 10.8a15.1 15.1 0 0 0 6.6 6.6l2.2-2.2c.3-.3.7-.4 1-.2 1.1.4 2.3.6 3.6.6.6 0 1 .4 1 1V20c0 .6-.4 1-1 1A17 17 0 0 1 3 4c0-.6.4-1 1-1h3.5c.6 0 1 .4 1 1 0 1.3.2 2.5.6 3.6.1.3 0 .7-.2 1z"/></svg>
        <span>+2 (0222) 45-678-90</span>
      </li>
      <li class="contact__item">
        <svg class="contact__icon" viewBox="0 0 24 24"><path fill="#fff" d="M3 5h18v14H3z"/><path fill="none" stroke="#2a74cc" stroke-width="1.8" d="M3 5l9 7 9-7"/></svg>
        <span>hello@sampledomain.com</span>
      </li>
      <li class="contact__item">
        <svg class="contact__icon" viewBox="0 0 24 24" fill="none" stroke="#fff" stroke-width="1.8"><circle cx="12" cy="12" r="9"/><ellipse cx="12" cy="12" rx="4" ry="9"/><path d="M3 12h18M5 7h14M5 17h14"/></svg>
        <span>www.sampledomain.com</span>
      </li>
      <li class="contact__item">
        <svg class="contact__icon" viewBox="0 0 24 24"><path fill="#fff" d="M12 3l10 9h-3v9h-5v-6h-4v6H5v-9H2z"/></svg>
        <span>148 Harbour Lane,<br>Riverton, USA</span>
      </li>
    </ul>

    <div class="divider"></div>

    <div class="person">
      <p class="person__name">Dana Whitfield</p>
      <p class="person__role">General Manager</p>
    </div>
  </article>
</main>
</body>
</html>
```